Interactive medical research website - INFOGRAPHIC

We are a non-profit developing HealWayLoop, the world's first online, interactive website dedicated to repurposing research (medical research using existing drugs, devices, and nutriceuticals to create new treatments) , and launching in beta at the end of the month. We need an infographic showing the flow of HealWayLoop for use on web and print materials introducing the site.

In the attached document, I provide the information we want represented, which is basically: what goes in, what happens, what comes out, and the ultimate goal. This could be represented in any number of ways through metaphor (a machine, and spinning top, etc) and would ideally show speed or acceleration as a part of the process.

Specific colors already in use are on document as well. Fonts are: century gothic (for print) and proximal (for web) - either would be fine.
Updates

Hi Designers - would love to receive your ideas today! Thank you!

Target Market(s)

science, philanthropy, healthcare industry

Industry/Entity Type

Non-Profit

Requirements
Must have
• clear flow, excitement
• use colors from attached document
Nice to have
• a good metaphor - HealWayLoopTM as a hub, an actual accelerator, an action tank of some kind

```html
<!DOCTYPE html>
<html lang="en">
<head>
<meta charset="utf-8">
<title>HealWayLoop – How It Works</title>
<link rel="stylesheet" href="https://fonts.googleapis.com/css2?family=Questrial&family=Didact+Gothic&display=swap">
<style>
  :root{
    --magenta:#e0197d;
    --lime:#8dc63f;
    --teal:#1ab3a6;
    --forest:#1f4d3a;
    --blue:#1a5ea8;
    --ink:#2b2b2b;
    --panel:#f4f4f4;
    --dash:#a9d36b;
    --grey:#b9b9b9;
    --goal:#b8d86e;
    --orange:#f5962a;
    --purple:#7b3f98;
  }
  *{margin:0;padding:0;box-sizing:border-box}
  html,body{width:1200px;height:1069px;overflow:hidden;background:#fff}
  body{font-family:"Questrial","Didact Gothic",sans-serif;color:var(--ink);position:relative}
  .canvas{position:absolute;inset:0}
  .abs{position:absolute}
  .heading{font-size:15.5px;font-weight:700;letter-spacing:.3px;line-height:1}
  .list{font-size:14.5px;line-height:17.3px;color:#333}
  .people .heading{color:var(--magenta)}
  .dollars .heading{color:var(--lime)}
  .repurposing .heading{color:var(--forest)}
  .products .heading{color:var(--teal)}
  .resources .heading{color:var(--blue)}
  .list p{margin:0}
  .brand{left:834px;top:470px;font-size:34px;letter-spacing:1px;color:var(--blue);font-family:"Questrial",sans-serif}
  .brand sup{font-size:12px;vertical-align:top;position:relative;top:2px}
  .hub-text{left:208px;width:340px;text-align:center;font-size:17px;color:#333;line-height:21px}
  .outcomes{left:784px;top:628px;width:290px;list-style:none;font-size:14.5px;line-height:17px;color:#333}
  .outcomes li{position:relative;padding-left:18px;margin-bottom:16.5px}
  .outcomes li::before{content:"";position:absolute;left:0;top:5px;width:7px;height:7px;border-radius:50%;background:var(--magenta)}
  .goal{left:752px;top:876px;width:328px;height:84px;border:1.5px dashed #fff;border-radius:6px;display:flex;align-items:center;justify-content:center;text-align:center;font-weight:700;font-size:16.5px;line-height:22px;color:#111;font-family:"Didact Gothic",sans-serif}
</style>
</head>
<body>
<div class="canvas">
  <svg class="abs" width="1200" height="1069" viewBox="0 0 1200 1069" aria-hidden="true">
    <!-- inputs panel -->
    <path d="M140 98 H1078 Q1090 98 1090 110 V404 Q1090 416 1078 416 H418 L380 452 L364 416 H140 Q128 416 128 404 V110 Q128 98 140 98 Z" fill="var(--panel)"/>
    <path d="M148 108 H1070 Q1080 108 1080 118 V396 Q1080 406 1070 406 H412 L382 436 L370 406 H148 Q138 406 138 396 V118 Q138 108 148 108 Z" fill="none" stroke="var(--dash)" stroke-width="1.3" stroke-dasharray="4 4"/>
    <!-- funnel -->
    <path d="M322 456 H416 L386 488 V506 H352 V488 Z" fill="#d9d9d9"/>
    <rect x="352" y="506" width="34" height="20" fill="#c4c4c4"/>
    <!-- hub -->
    <circle cx="372" cy="742" r="236" fill="#e9e9e9"/>
    <circle cx="372" cy="742" r="228" fill="var(--teal)"/>
    <circle cx="380" cy="745" r="176" fill="#fff"/>
    <!-- gears -->
    <g fill="none" stroke="var(--lime)" stroke-width="7" stroke-dasharray="5 4">
      <circle cx="338" cy="622" r="19"/>
    </g>
    <circle cx="338" cy="622" r="14" fill="var(--lime)"/>
    <circle cx="338" cy="622" r="5" fill="var(--magenta)"/>
    <g fill="none" stroke="var(--teal)" stroke-width="6" stroke-dasharray="4 3.5">
      <circle cx="382" cy="634" r="15"/>
    </g>
    <circle cx="382" cy="634" r="11" fill="var(--teal)"/>
    <circle cx="382" cy="634" r="4" fill="#fff"/>
    <!-- connector -->
    <rect x="608" y="690" width="142" height="20" rx="4" fill="#d4d4d4"/>
    <rect x="624" y="698" width="64" height="4" fill="var(--lime)"/>
    <rect x="688" y="698" width="48" height="4" fill="#444"/>
    <circle cx="744" cy="700" r="12" fill="#fff" stroke="#bdbdbd" stroke-width="3"/>
    <!-- outcomes box -->
    <rect x="752" y="616" width="336" height="170" rx="8" fill="var(--panel)"/>
    <rect x="760" y="624" width="320" height="154" rx="6" fill="none" stroke="var(--dash)" stroke-width="1.3" stroke-dasharray="4 4"/>
    <!-- droplet triangle -->
    <g fill="var(--lime)">
      <circle cx="894" cy="800" r="5"/><circle cx="906" cy="800" r="5"/><circle cx="918" cy="800" r="5"/><circle cx="930" cy="800" r="5"/><circle cx="942" cy="800" r="5"/>
      <circle cx="900" cy="811" r="5"/><circle cx="912" cy="811" r="5"/><circle cx="924" cy="811" r="5"/><circle cx="936" cy="811" r="5"/>
      <circle cx="906" cy="822" r="5"/><circle cx="918" cy="822" r="5"/><circle cx="930" cy="822" r="5"/>
      <circle cx="912" cy="833" r="5"/><circle cx="924" cy="833" r="5"/>
    </g>
    <rect x="882" y="846" width="42" height="20" fill="var(--goal)"/>
    <!-- goal box -->
    <rect x="740" y="864" width="352" height="108" rx="10" fill="var(--goal)"/>
    <!-- icons -->
    <rect x="156" y="156" width="72" height="62" rx="4" fill="var(--magenta)" role="img" aria-label="Icon of two people"/>
    <rect x="164" y="326" width="56" height="32" rx="2" fill="none" stroke="var(--lime)" stroke-width="3"/>
    <rect x="170" y="332" width="44" height="20" fill="none" stroke="var(--lime)" stroke-width="1.5"/>
    <text x="176" y="348" font-size="16" font-weight="700" fill="var(--lime)" font-family="Questrial,sans-serif">$</text>
    <rect x="618" y="150" width="76" height="54" rx="4" fill="var(--forest)" role="img" aria-label="Icon of a network of people around documents"/>
    <g transform="rotate(-30 662 243)">
      <rect x="636" y="232" width="52" height="22" rx="11" fill="var(--teal)"/>
      <path d="M662 232 H677 A11 11 0 0 1 677 254 H662 Z" fill="#fff" stroke="var(--teal)" stroke-width="2"/>
    </g>
    <rect x="648" y="302" width="30" height="40" rx="3" fill="none" stroke="var(--blue)" stroke-width="3"/>
    <rect x="657" y="298" width="12" height="7" rx="2" fill="var(--blue)"/>
    <g stroke="var(--blue)" stroke-width="2">
      <line x1="654" y1="314" x2="672" y2="314"/><line x1="654" y1="322" x2="672" y2="322"/><line x1="654" y1="330" x2="672" y2="330"/>
    </g>
    <!-- brand mark -->
    <circle cx="768" cy="490" r="40" fill="var(--teal)"/>
  </svg>

  <section class="abs people" style="left:242px;top:148px">
    <h2 class="heading">PEOPLE</h2>
    <div class="list" style="margin:3px 0 0 26px">
      <p>Researchers</p><p>Clinicians</p><p>Philanthropists</p><p>Venture philanthropists</p><p>Industry professionals</p><p>Research institution staff</p><p>Foundations and disease specific non-profits</p><p>Patients</p>
    </div>
  </section>

  <section class="abs dollars" style="left:242px;top:322px">
    <h2 class="heading">DOLLARS</h2>
    <div class="list" style="margin:3px 0 0 26px">
      <p>Philanthropic funding, industry sponsorship,</p><p>research institution co-funding</p>
    </div>
  </section>

  <section class="abs repurposing" style="left:714px;top:150px">
    <h2 class="heading">REPURPOSING OPPORTUNITIES</h2>
    <div class="list" style="margin:3px 0 0 26px">
      <p>From researchers, clinicians, patients,</p><p>bioinformatics and industry</p>
    </div>
  </section>

  <section class="abs products" style="left:714px;top:222px">
    <h2 class="heading">PRODUCTS</h2>
    <div class="list" style="margin:3px 0 0 26px">
      <p>Drugs, Devices, Nutriceuticals, Diagnostics,</p><p>Therapies</p>
    </div>
  </section>

  <section class="abs resources" style="left:714px;top:293px">
    <h2 class="heading">MEMBER RESOURCES</h2>
    <div class="list" style="margin:3px 0 0 26px">
      <p>Regulatory expertise, Legal support, Trial</p><p>management, Manufacturing, Patient</p><p>enrollment</p>
    </div>
  </section>

  <div class="abs brand">HEALWAYLOOP<sup>TM</sup></div>

  <div class="abs hub-text" style="top:682px">Conversation forums</div>
  <div class="abs hub-text" style="top:722px">Requests for Proposals</div>
  <div class="abs hub-text" style="top:764px">Research Project Proposals/<br>Scientific Review<br>and Validation</div>

  <ul class="abs outcomes">
    <li>Funded proof of concept clinical trials</li>
    <li>Final preclinical research</li>
    <li>New collaborations</li>
    <li>A fast track from idea to testing to potential treatment</li>
  </ul>

  <div class="abs goal">Effective, affordable repurposed<br>treatments for patients in need</div>
</div>
</body>
</html>
```